New IPv6 service needs a Web Design

We're launching a brand new service which is designed to connect the current Internet Protocol (IPv4) to the new Internet Protocol (IPv6).
The logo can be found at http://www.brelvo-link.example
We're looking for a clean and simple design, nothing super-fancy. There has to be room for some menu items and a place where people can login (so an e-mail and password box and login button, which must be replaced by the username and a logout button when the user is logged in).
We need a place for a rotating billboard (see http://qa.zx for an example) or a video.
Designs that incorporate IPv4 - IPv6 elements (images with interconnecting networks, videos doing the same) will be rated higher, although the basic design is still the primary concern.
We need :
- A main page, with the rotating billboard and some other typical main page stuff
- 2 subpages with different formatted content blocks (1 column and 2 column)
This is a very short design contest, since we intend to go live very soon. Decision will be made quickly.
PSD file is sufficient, but it must be easy to slice to HTML/CSS (but we'll do that part ourselves).
Target Market(s)
IT Professionals
Industry/Entity Type
Internet
Look and feel
Each slider illustrates characteristics of the customer's brand and the style your logo design should communicate.

```html
<!DOCTYPE html>
<html lang="en">
<head>
<meta charset="utf-8">
<title>Brelvo – IPv6 New Internet Protocol</title>
<link rel="stylesheet" href="https://fonts.googleapis.com/css2?family=Arimo:wght@400;700&family=Didact+Gothic&display=swap">
<style>
:root{
  --ink:#333;
  --muted:#555;
  --brand-blue:#1a6aa6;
  --link-blue:#1c6fb0;
  --nav-bg:#f1f1f1;
  --line:#d8d8d8;
  --hero-bg:#f3f3f3;
  --button:#1a73b8;
  --button-dark:#0d568f;
  --accent-red:#d4242b;
  --footer-bg:#f4f4f4;
  --bottom-bg:#cfcfcf;
  --white:#fff;
}
*{box-sizing:border-box;margin:0;padding:0}
html,body{width:1200px;height:930px;overflow:hidden}
body{position:relative;background:var(--white);font-family:"Arimo",Arial,sans-serif;color:var(--ink)}
a{color:inherit;text-decoration:none}
.abs{position:absolute}

.topbar{left:0;top:0;width:1200px;height:32px;background:#f7f7f7;box-shadow:0 2px 4px rgba(0,0,0,.12);font-size:12px}
.topbar .inner{position:absolute;right:194px;top:9px;display:flex;gap:14px;align-items:center}
.topbar .phone{color:var(--brand-blue);font-size:13.5px}
.topbar .register{font-weight:700}
.topbar .sep{color:#666}

.logo-box{left:193px;top:23px;width:236px;height:127px;background:var(--white);border:1px solid #ccc;z-index:3;display:flex;align-items:center;justify-content:center;gap:8px}
.logo-box .mark{width:14px;height:14px;border-radius:50%;background:var(--brand-blue)}
.logo-box .name{font-size:38px;font-weight:700;color:var(--brand-blue)}

.search{left:753px;top:45px;width:271px;height:29px;border:1px solid #ccc;background:var(--white)}
.search span{position:absolute;left:10px;top:8px;font-size:11px;font-style:italic;color:#777}
.search .btn{position:absolute;right:-1px;top:-1px;width:29px;height:29px;background:var(--button)}

.nav{left:480px;top:86px;height:38px;display:flex;border:1px solid #ccc;border-radius:3px;background:linear-gradient(#fafafa,#ececec)}
.nav a{display:flex;align-items:center;justify-content:center;font-size:13px;letter-spacing:.4px;color:#444;border-right:1px solid #d2d2d2}
.nav a:last-child{border-right:0}
.nav .active{font-weight:700}

.hero{left:0;top:138px;width:1200px;height:316px;background:radial-gradient(ellipse at 40% 50%,#fff 0%,var(--hero-bg) 60%,#e8e8e8 100%);border-top:1px solid #ddd;border-bottom:1px solid #ccc}
.hero-art{left:265px;top:25px;width:388px;height:290px;background:radial-gradient(ellipse at 60% 60%,#f3e1d0 0%,#eef1f7 40%,#f6f6f6 75%);border-radius:4px}
.hero-title{left:797px;top:20px;font-family:"Didact Gothic",Arial,sans-serif;font-size:30px;line-height:31px;color:#444}
.hero-text{left:799px;top:131px;width:200px;font-size:13.5px;line-height:14.5px;color:#444}
.hero-btn{left:797px;top:201px;width:140px;height:34px;border-radius:3px;background:linear-gradient(var(--button),var(--button-dark));border:1px solid #0b4a7a;color:var(--white);font-size:15px;display:flex;align-items:center;justify-content:center}
.dots{left:845px;top:287px;display:flex;gap:11px}
.dots i{width:12px;height:12px;border-radius:50%;background:#a9c2d6;border:1px solid #7d9db7}
.dots i.on{background:var(--brand-blue);border-color:#0b4a7a}

.card{top:476px;width:273px;height:225px;border:1px solid var(--line);border-radius:3px;background:linear-gradient(#fff,#f9f9f9)}
.card h2{position:absolute;left:19px;top:16px;font-weight:400;font-size:15.5px;color:var(--link-blue)}
.card .rule{position:absolute;left:19px;right:19px;top:44px;border-top:1px solid var(--line)}
.card p{position:absolute;left:18px;width:236px;font-size:11.4px;line-height:12.8px;color:#444;text-align:justify}
.card .lead{top:55px}
.card .tail{top:130px;width:110px;text-align:left}
.card .thumb{position:absolute;left:135px;top:104px;width:117px;height:100px;border:1px solid #ccc}
.card .more{position:absolute;left:18px;top:200px;font-size:11.5px;color:#555;display:flex;align-items:center;gap:10px}
.card .more i{width:11px;height:11px;border-radius:50%;background:var(--accent-red);position:relative}
.card .more i::after{content:"";position:absolute;left:3px;top:3px;border:3px solid transparent;border-left:4px solid #fff;border-right:0}
.card .video{position:absolute;left:25px;top:57px;width:224px;height:150px;border:1px solid #ccc;background:radial-gradient(ellipse at 45% 40%,#e4ebf7,#fafafa 70%)}
.video .play{position:absolute;left:94px;top:52px;width:40px;height:30px;background:rgba(30,30,30,.75);border-radius:3px}
.video .play::after{content:"";position:absolute;left:15px;top:8px;border:7px solid transparent;border-left:11px solid #fff;border-right:0}
.video .full{position:absolute;left:12px;top:124px;width:20px;height:17px;background:#555;border-radius:3px}

.footer{left:0;top:726px;width:1200px;height:160px;background:linear-gradient(#fbfbfb,var(--footer-bg));border-top:1px solid #e3e3e3}
.col{top:18px}
.col h3{font-weight:400;font-size:13.2px;letter-spacing:.2px;color:#333;margin-bottom:10px}
.col li{list-style:none;font-size:11.6px;color:#555;line-height:21.2px;padding-left:1px}
.signup input{display:block;width:150px;height:24px;border:1px solid #ccc;background:#fff;margin:2px 0 16px}
.signup p{font-size:11.6px;line-height:13px;color:#444;width:160px}
.signup b{color:#555}
.social .badge{width:91px;height:29px;margin-bottom:7px;border-radius:2px;display:flex;align-items:center;gap:6px;padding-left:8px;color:#fff;font-size:12.5px;font-weight:700}
.social .c1{background:#3fa8d8}
.social .c2{background:#3d5a98}
.social .c3{color:#111;padding-left:1px;font-size:14px}
.social .badge i{width:9px;height:9px;background:#fff;display:block}

.bottom{left:0;top:886px;width:1200px;height:44px;background:var(--bottom-bg);font-size:11.5px;color:#444}
.bottom .copy{position:absolute;left:195px;top:16px;display:flex;gap:14px;align-items:center}
.bottom .brand{font-size:19px;font-weight:700;color:var(--brand-blue);margin-top:-4px}
.bottom .legal{position:absolute;right:62px;top:16px;display:flex;gap:18px}
</style>
</head>
<body>

<header>
  <div class="abs topbar">
    <div class="inner">
      <span>Customer Service <span class="phone">(555) 010-2040</span></span>
      <span class="sep">|</span><a href="#">Support</a>
      <span class="sep">|</span><a href="#">Login</a>
      <span class="sep">/</span><a class="register" href="#">Register</a>
    </div>
  </div>

  <div class="abs logo-box"><span class="mark"></span><span class="name">Brelvo</span></div>

  <div class="abs search"><span>Search</span>
    <div class="btn">
      <svg width="29" height="29" viewBox="0 0 29 29"><circle cx="13" cy="13" r="6" fill="none" stroke="#fff" stroke-width="2.4"/><line x1="17.5" y1="17.5" x2="22" y2="22" stroke="#fff" stroke-width="2.6" stroke-linecap="round"/></svg>
    </div>
  </div>

  <nav class="abs nav">
    <a class="active" href="#" style="width:85px">HOME</a>
    <a href="#" style="width:121px">PRODUCTS</a>
    <a href="#" style="width:116px">SERVICES</a>
    <a href="#" style="width:118px">ABOUT US</a>
    <a href="#" style="width:101px">CONTACT</a>
  </nav>
</header>

<section class="abs hero">
  <div class="abs hero-art" role="img" aria-label="Hand drawing a network of connected user icons"></div>
  <h1 class="abs hero-title" style="font-weight:400">IPv6 -<br>New Internet<br>Protocol</h1>
  <p class="abs hero-text">Lorem Ipsum. Proin gravida nibh vel velit auctor aliquet. Aenean sollicitudin, lorem</p>
  <a class="abs hero-btn" href="#">Read More</a>
  <div class="abs dots"><i></i><i class="on"></i><i></i><i></i></div>
</section>

<main>
  <article class="abs card" style="left:176px">
    <h2>IPv6 - New Internet Protocol</h2><div class="rule"></div>
    <p class="lead">Lorem Ipsum. Proin gravida nibh vel velit auctor aliquet. Aenean sollicitudin, lorem quis bibendum auctor, nisi elit consequat ipsum, nec sagittis<br>sem nibh id elit.</p>
    <p class="tail">Duis sed odio.<br>sit amet nibh<br>vulputate cursus</p>
    <div class="thumb" role="img" aria-label="Person sketching internet protocol diagram" style="background:linear-gradient(90deg,#f4f4f4,#e9e3df 60%,#c9b6a8)"></div>
    <a class="more" href="#">Read more <i></i></a>
  </article>

  <article class="abs card" style="left:465px">
    <h2>A More Secure Protocol</h2><div class="rule"></div>
    <p class="lead">Lorem Ipsum. Proin gravida nibh vel velit auctor aliquet. Aenean sollicitudin, lorem quis bibendum auctor, nisi elit consequat ipsum, nec sagittis<br>sem nibh id elit.</p>
    <p class="tail">Duis sed odio.<br>sit amet nibh<br>vulputate cursus</p>
    <div class="thumb" role="img" aria-label="Word cloud about data security with chain and padlock" style="background:linear-gradient(135deg,#e8eee2,#c9c9c4 50%,#e3e6de)"></div>
    <a class="more" href="#">Read more <i></i></a>
  </article>

  <article class="abs card" style="left:751px">
    <h2>Watch How It Works</h2><div class="rule"></div>
    <div class="video" role="img" aria-label="Video still of IPv6 lettering connected to a computer mouse">
      <span class="play"></span><span class="full"></span>
    </div>
  </article>
</main>

<footer>
  <div class="abs footer">
    <div class="abs col" style="left:192px"><h3>COMPANY</h3><ul><li>About Us</li><li>History</li><li>Management</li><li>Leadership</li><li>Our Mission</li></ul></div>
    <div class="abs col" style="left:326px"><h3>EXPERTISE</h3><ul><li>Internet Protocols</li><li>Certifications</li><li>Networking</li><li>Consulting</li><li>Technology</li></ul></div>
    <div class="abs col" style="left:465px"><h3>MY ACCOUNT</h3><ul><li>Login</li><li>Register</li><li>Help</li></ul></div>
    <div class="abs col signup" style="left:613px"><h3>EMAIL SIGN UP</h3><input type="text" aria-label="Email"><p>Sign up and we'll keep you updated with the latest <b>Brelvo</b> updates and news</p></div>
    <div class="abs col social" style="left:805px"><h3>SOCIAL</h3>
      <div class="badge c1"><i></i>Chirpline</div>
      <div class="badge c2"><i></i>Friendwall</div>
      <div class="badge c3">Workgraph</div>
    </div>
    <div class="abs col" style="left:935px"><h3>CONNECT</h3><ul><li>Contact</li><li>Brochure</li><li>FAQs</li><li>Downloads</li></ul></div>
  </div>
  <div class="abs bottom">
    <div class="copy"><span>Copyright © 2012</span><span class="brand">Brelvo</span><span><b>Brelvo.</b>&nbsp; All Rights Reserved</span></div>
    <div class="legal"><a href="#">Privacy Policy</a><a href="#">Term of Use</a></div>
  </div>
</footer>

</body>
</html>
```